Business Card Design

Company is a Commercial Building Company specialising in New Construction and existing refurbishments

Business

Contact Information for Business Card

Derek Halloway
Construction Manager
E Derek@ridgemarkbuilding.com.au
M 0400 215 397
Mail 14 Tarrington Loop Marlow Bay WA 6182

```html
<!DOCTYPE html>
<html lang="en">
<head>
<meta charset="utf-8">
<title>Ridgemark Building &amp; Construction — Business Card</title>
<link rel="stylesheet" href="https://fonts.googleapis.com/css2?family=Saira+Semi+Condensed:wght@400;600&family=Roboto:wght@400;500;700&display=swap">
<style>
  :root {
    --backdrop: #e5e3e0;
    --navy: #2e3447;
    --navy-light: #4a5166;
    --cyan: #1bb3d6;
    --orange: #f28c1e;
    --white: #ffffff;
    --text-grey: #3b4050;
  }
  * { box-sizing: border-box; margin: 0; padding: 0; }
  html, body {
    width: 1200px; height: 997px; overflow: hidden;
    background: var(--backdrop);
  }
  .canvas { position: relative; width: 1200px; height: 997px; }

  .card {
    position: absolute;
    width: 560px; height: 340px;
    box-shadow: 0 10px 28px rgba(0,0,0,0.18);
    overflow: hidden;
  }

  /* Front */
  .card-front {
    left: 90px; top: 120px;
    background: radial-gradient(circle at 50% 42%, var(--navy-light) 0%, var(--navy) 70%);
    display: flex; align-items: center; justify-content: center;
  }
  .front-name {
    font-family: "Saira Semi Condensed", sans-serif;
    font-weight: 600;
    color: var(--white);
    font-size: 32px;
    line-height: 1.05;
    letter-spacing: 1px;
    text-transform: uppercase;
    text-align: left;
  }

  /* Back */
  .card-back { left: 550px; top: 520px; background: var(--white); }
  .card-back .bands { position: absolute; inset: 0; }

  .brand {
    position: absolute; left: 36px; top: 72px;
    display: flex; align-items: flex-start; gap: 9px;
  }
  .brand-mark { width: 14px; height: 14px; background: var(--cyan); margin-top: 4px; }
  .brand-name {
    font-family: "Saira Semi Condensed", sans-serif;
    font-weight: 600;
    color: var(--navy);
    font-size: 19px; line-height: 1.05;
    text-transform: uppercase;
  }
  .brand-rule { position: absolute; left: 36px; top: 130px; width: 226px; height: 1.5px; background: var(--cyan); }
  .link-rule { position: absolute; left: 272px; top: 110px; width: 118px; height: 1.5px; background: var(--orange); }

  .person {
    position: absolute; right: 36px; top: 66px; text-align: right;
    font-family: "Roboto", sans-serif; color: var(--navy);
  }
  .person-name { font-weight: 700; font-size: 16px; letter-spacing: 0.5px; text-transform: uppercase; }
  .person-title { font-size: 11px; margin-top: 2px; }

  .address {
    position: absolute; right: 36px; top: 130px; text-align: right;
    font-family: "Roboto", sans-serif; font-size: 13px; line-height: 1.4; color: var(--text-grey);
  }

  .contacts {
    position: absolute; left: 36px; top: 172px; list-style: none;
    font-family: "Roboto", sans-serif; font-size: 13px; line-height: 1.45; color: var(--text-grey);
  }
  .contacts li { display: flex; align-items: center; gap: 8px; }
  .contacts svg { width: 12px; height: 12px; flex: none; }
</style>
</head>
<body>
<main class="canvas">

  <section class="card card-front" aria-label="Card front">
    <p class="front-name">Ridgemark Building<br>&amp; Construction</p>
  </section>

  <section class="card card-back" aria-label="Card back">
    <svg class="bands" viewBox="0 0 560 340" aria-hidden="true">
      <polygon fill="var(--orange)" points="0,248 305,248 335,208 560,208 560,262 0,262"/>
      <polygon fill="var(--cyan)" points="0,268 316,268 300,292 0,292"/>
    </svg>

    <div class="brand">
      <span class="brand-mark"></span>
      <p class="brand-name">Ridgemark Building<br>&amp; Construction</p>
    </div>
    <span class="brand-rule"></span>
    <span class="link-rule"></span>

    <div class="person">
      <p class="person-name">Derek Halloway</p>
      <p class="person-title">Construction Manager</p>
    </div>

    <p class="address">14 Tarrington Loop<br>Marlow Bay WA 6182</p>

    <ul class="contacts">
      <li>
        <svg viewBox="0 0 12 12" aria-hidden="true"><rect x="2.5" y="0.75" width="7" height="10.5" rx="1.2" fill="none" stroke="var(--navy)" stroke-width="1.3"/></svg>
        0400 215 397
      </li>
      <li>
        <svg viewBox="0 0 12 12" aria-hidden="true"><rect x="0.75" y="2" width="10.5" height="8" fill="var(--navy)"/><polyline points="0.75,2 6,6.5 11.25,2" fill="none" stroke="var(--white)" stroke-width="1"/></svg>
        Derek@ridgemarkbuilding.com.au
      </li>
    </ul>
  </section>

</main>
</body>
</html>
```